Dental Business Card

We are looking for a double sided business card that can be easily customized with the names of the different members of our dental team.

I would like the background to be the 2-tone blue fleur-de-lis type pattern on the sides of our website (www.harborlanegrins.com).

I would like the logo attached incorporated.

I would like our address (4872 Pell Orchard Drive, Suite 100, Williamsburg, VA 23412), phone number (757-318-4590), fax number (757-318-2764), website (www.harborlanegrins.com), and email address (info@harborlanegrins.com) all included on the front side.

Something a little more artistic to complement/highlight the logo on the back would be interesting.

I would like the business card to look professional, slightly feminine, and expense.

Reason: Still looking for the perfect design.

```html
<!DOCTYPE html>
<html lang="en">
<head>
<meta charset="utf-8">
<title>Harbor Lane Grins – Business Card</title>
<link href="https://fonts.googleapis.com/css2?family=Cinzel:wght@500&family=Mukta:wght@400&display=swap" rel="stylesheet">
<style>
  :root {
    --page: #e6e6e4;
    --card-blue: #c8dae8;
    --card-blue-deep: #b7cde0;
    --ink-blue: #1f4fa0;
    --rule-blue: #3c7fd0;
    --back-black: #050505;
    --white: #ffffff;
  }
  * { margin: 0; padding: 0; box-sizing: border-box; }
  html, body { width: 1200px; height: 1000px; overflow: hidden; }
  body { background: var(--page); position: relative; }

  .card {
    position: absolute;
    left: 250px;
    width: 700px;
    height: 400px;
    box-shadow: 0 6px 18px rgba(0,0,0,0.18);
  }

  /* Back side */
  .card--back { top: 60px; background: var(--card-blue); padding: 14px; }
  .card--back .back-panel {
    position: relative;
    width: 100%;
    height: 100%;
    background: var(--back-black);
  }
  .card--back .back-name {
    position: absolute;
    right: 34px;
    bottom: 40px;
    font-family: "Cinzel", serif;
    font-weight: 500;
    font-size: 34px;
    color: var(--white);
    letter-spacing: 1px;
  }

  /* Front side */
  .card--front { top: 540px; overflow: hidden; }
  .card-pattern {
    position: absolute; inset: 0;
    background: linear-gradient(135deg, var(--card-blue) 0%, var(--card-blue-deep) 100%);
  }
  .card-content { position: absolute; inset: 0; }

  .brand-header {
    position: absolute; left: 0; right: 0; top: 34px;
    text-align: center;
    color: var(--ink-blue);
    font-family: "Cinzel", serif;
    font-weight: 500;
  }
  .brand-header .brand-name { font-size: 26px; letter-spacing: 1px; line-height: 1; }
  .brand-header .brand-tagline { font-size: 10.5px; letter-spacing: 1.5px; margin-top: 3px; }
  .header-rule {
    position: absolute; left: 0; right: 0; top: 90px;
    height: 1.5px; background: var(--rule-blue);
  }
  .address {
    position: absolute; left: 40px; top: 104px;
    font-family: "Mukta", sans-serif;
    font-size: 15px; letter-spacing: 1px;
    text-transform: uppercase;
    color: var(--ink-blue);
  }
  .mark-name {
    position: absolute; right: 40px; top: 170px;
    font-family: "Cinzel", serif; font-weight: 500;
    font-size: 30px; color: var(--ink-blue);
    text-align: right; line-height: 1.15;
  }

  .contact-list {
    position: absolute; left: 40px; bottom: 40px;
    list-style: none;
    font-family: "Mukta", sans-serif;
    font-size: 23px;
    color: var(--ink-blue);
  }
  .contact-list li { display: flex; align-items: center; gap: 12px; line-height: 1.28; }
  .contact-list svg { width: 17px; height: 17px; fill: var(--ink-blue); flex: none; }
</style>
</head>
<body>

<section class="card card--back" aria-label="Card back">
  <div class="back-panel">
    <span class="back-name">Harbor Lane Grins</span>
  </div>
</section>

<section class="card card--front" aria-label="Card front">
  <div class="card-pattern" role="img" aria-label="Two-tone pale blue fleur-de-lis damask pattern"></div>
  <div class="card-content">
    <header class="brand-header">
      <div class="brand-name">Harbor Lane Grins</div>
      <div class="brand-tagline">THE ART OF DENTISTRY</div>
    </header>
    <div class="header-rule"></div>
    <p class="address">4872 Pell Orchard Drive, Suite 100, Williamsburg, VA 23412</p>

    <div class="mark-name">Harbor Lane<br>Grins</div>

    <ul class="contact-list">
      <li>
        <svg viewBox="0 0 24 24" aria-hidden="true"><path d="M6.6 10.8a15.1 15.1 0 0 0 6.6 6.6l2.2-2.2c.3-.3.7-.4 1-.2 1.1.4 2.3.6 3.6.6.6 0 1 .4 1 1V20c0 .6-.4 1-1 1A17 17 0 0 1 3 4c0-.6.4-1 1-1h3.5c.6 0 1 .4 1 1 0 1.3.2 2.5.6 3.6.1.3 0 .7-.2 1z"/></svg>
        757-318-4590
      </li>
      <li>
        <svg viewBox="0 0 24 24" aria-hidden="true"><path d="M6 2h9l3 3v4H6zM3 10h18a1 1 0 0 1 1 1v7h-4v4H6v-4H2v-7a1 1 0 0 1 1-1zm5 7v3h8v-3z"/></svg>
        757-318-2764
      </li>
      <li>
        <svg viewBox="0 0 24 24" aria-hidden="true"><path d="M2 5h20v1.5l-10 6.5L2 6.5zm0 3.8 10 6.4 10-6.4V19H2z"/></svg>
        info@harborlanegrins.com
      </li>
      <li>
        <svg viewBox="0 0 24 24" aria-hidden="true"><path d="M14 2a8 8 0 1 1-4.9 14.3L3.4 22 2 20.6l5.7-5.7A8 8 0 0 1 14 2zm0 2.5a5.5 5.5 0 1 0 0 11 5.5 5.5 0 0 0 0-11z"/></svg>
        www.harborlanegrins.com
      </li>
    </ul>
  </div>
</section>

</body>
</html>
```